Granite Tile Retail Website

We need wireframe PSD for a website selling granite tile. There are 4 custom pages, shopping cart page, and checkout page. I have a logo designed but the color scheme is up to you.
Please look at design-explanation.docx as I got through each page with more detail.
Home - I mocked up the home page so you know the layout (lg-home.jpg). This is where I need you to spend the most time to make a very appealing design.
Color Gallery - We have approximately 20 different stone colors. Each color will have a little gallery of its own pictures. On this page the customer can also add a sample piece of the color they are viewing to their shopping cart.
Questions Page - This page has 3 elements
1. Upload or fax diagram of kitchen for quotation
2. Installation video
3. Installation FAQ (text)
Order Page - This page has 3 steps for the customer
1. Customer chooses his color.
2. For each color we have numerous different products. He inputs the quantity of each product.
3. Customer is given total price and shipping quote. If order over $500 it says "This order qualifies for free shipping". Customer can click on button to "Order Now"
Shopping Cart - Very standard, just like I have attached here. Just modify for your colors / font.
Checkout - Just like in the attached. See design-explanation.docx for minor adjustments.
I have vector file for logo.
Updates
Please try to post your designs by tonightÂ
Target Market(s)
Home owners 40-60 years old
Industry/Entity Type
Shopping
Look and feel

```html
<!DOCTYPE html>
<html lang="en">
<head>
<meta charset="utf-8">
<title>Stonecrest – Orders</title>
<link href="https://fonts.googleapis.com/css2?family=Arimo:wght@400;700&family=PT+Serif:wght@400;700&display=swap" rel="stylesheet">
<style>
:root{
  --teal:#4f8f8b;
  --teal-dark:#3c7470;
  --teal-deep:#356864;
  --gold:#f2b318;
  --gold-dark:#d99a0c;
  --ink:#2b2b2b;
  --muted:#555;
  --panel:#f2f2f2;
  --line:#c9c9c9;
  --white:#fff;
  --link:#2a7fc9;
  --footer-text:#e4efee;
}
*{box-sizing:border-box;margin:0;padding:0}
html,body{width:1200px;height:1155px;overflow:hidden}
body{position:relative;background:var(--white);font-family:"Arimo",Arial,sans-serif;color:var(--ink);font-size:12px}
.abs{position:absolute}
.site-header{position:absolute;left:0;top:0;width:1200px;height:93px;background:linear-gradient(var(--teal-dark) 0 5px,var(--teal) 5px)}
.brand{position:absolute;left:262px;top:30px;display:flex;align-items:center;gap:10px;color:var(--white);font-family:"Arimo",sans-serif;font-weight:700;font-size:22px;letter-spacing:1px}
.brand-mark{width:22px;height:22px;background:var(--gold)}
.nav a{position:absolute;top:65px;color:var(--white);font-weight:700;font-size:11px;text-decoration:none}
.nav a.active{left:497px;top:57px;width:63px;height:30px;line-height:30px;text-align:center;background:var(--gold);color:#5a3c00;border-radius:3px}
.mini-cart{position:absolute;left:854px;top:0;width:102px;height:29px;background:var(--teal-deep);border-radius:0 0 4px 4px;display:flex;align-items:center;gap:6px;padding-left:8px}
.mini-cart i{width:15px;height:15px;border-radius:50%;background:var(--gold)}
.mini-cart span{font-size:7px;line-height:9px;color:var(--white)}
.mini-cart b{color:var(--gold)}
.hero-band{position:absolute;left:0;top:93px;width:1200px;height:130px;background:linear-gradient(#d6d6d6,#fff)}
.page-title{position:absolute;left:250px;top:128px;font-family:"PT Serif",serif;font-size:27px;font-weight:400;display:flex;align-items:center;gap:10px}
.page-title i{width:14px;height:14px;border:2px solid #444}
.panel{position:absolute;left:240px;top:185px;width:720px;height:823px;background:var(--panel);border:1px solid #dcdcdc}
.panel-foot{position:absolute;left:240px;top:1003px;width:720px;height:6px;background:#cfcfcf}
.head-row{position:absolute;left:241px;width:718px;height:38px;background:var(--white)}
.step{position:absolute;width:18px;height:18px;border-radius:50%;background:#f1ead0;border:1px solid #a9a48f;font-family:"PT Serif",serif;font-size:11px;line-height:16px;text-align:center;color:#555}
.step-title{position:absolute;font-family:"PT Serif",serif;font-weight:700;font-size:15px;color:#222}
.field{position:absolute;height:21px;background:var(--white);border:1px solid #b5b5b5;font-size:12px;padding:3px 6px;color:#444}
.select{position:absolute;height:21px;background:var(--white);border:1px solid #b5b5b5;font-size:12px;padding:3px 6px;color:#555;overflow:hidden;white-space:nowrap}
.select::after{content:"";position:absolute;right:0;top:0;width:20px;height:19px;background:#555}
.select svg{position:absolute;right:5px;top:6px;z-index:1}
.lbl{position:absolute;font-size:12px;color:#222;white-space:nowrap}
.qty-lbl{position:absolute;left:514px;font-size:10px;color:#222}
.qty{position:absolute;left:591px;width:62px;height:15px;background:var(--white);border:1px solid #b5b5b5}
.swatch{position:absolute;width:43px;height:38px}
.sub-title{position:absolute;left:262px;top:331px;font-family:"PT Serif",serif;font-weight:700;font-size:13px}
.price-card{position:absolute;left:759px;top:249px;width:182px;height:152px;background:#fafafa;border:1px solid #e1e1e1;border-radius:8px}
.btn-cart{position:absolute;left:785px;top:348px;width:123px;height:27px;background:var(--teal);border-radius:4px 14px 14px 4px;color:var(--white);font-weight:700;font-size:11px;line-height:27px;padding-left:37px;white-space:nowrap}
.btn-cart i{position:absolute;left:-2px;top:-2px;width:31px;height:31px;border-radius:50%;background:var(--gold)}
.radio{position:absolute;width:15px;height:15px;border-radius:50%;background:#e6e6e6;border:1px solid #bbb}
.radio.on{background:radial-gradient(circle,#2f7fd6 0 4px,#cfe2f7 5px)}
.check{position:absolute;width:11px;height:11px}
.order-table{position:absolute;left:725px;top:532px;width:228px;border-collapse:collapse;font-size:8.5px}
.order-table th{font-weight:400;font-size:12px;height:22px;text-align:left;border-bottom:1px solid var(--line)}
.order-table td{height:23px;border-bottom:1px solid #dedede;color:#222}
.order-table tr.total td{height:18px;background:#e7e7e7;border-bottom:1px solid #fff}
.order-table .num{text-align:right;padding-right:2px}
.comments{position:absolute;left:726px;top:716px;width:200px;height:67px;background:var(--white);border:1px solid #b5b5b5}
.small{font-size:10px}
.link{color:var(--link);text-decoration:underline}
.btn-order{position:absolute;left:831px;top:848px;width:91px;height:23px;border-radius:12px;background:linear-gradient(#f7c54a,var(--gold-dark));font-size:9px;font-weight:700;text-align:center;line-height:23px;color:#4a3300;text-decoration:none}
.below-band{position:absolute;left:0;top:1009px;width:1200px;height:45px;background:linear-gradient(#fff,#dcdcdc)}
.site-footer{position:absolute;left:0;top:1054px;width:1200px;height:101px;background:linear-gradient(var(--teal-dark) 0 4px,var(--teal) 4px)}
.site-footer a{position:absolute;font-size:9px;font-weight:700;color:var(--footer-text);text-decoration:none;white-space:nowrap}
.foot-brand{position:absolute;left:873px;top:1074px;display:flex;align-items:center;gap:5px;color:var(--white);font-weight:700;font-size:12px;letter-spacing:1px}
.foot-brand i{width:10px;height:10px;background:var(--gold)}
.copy{position:absolute;left:840px;top:1114px;width:118px;text-align:right;font-size:9px;line-height:13px;color:var(--footer-text)}
</style>
</head>
<body>

<header class="site-header">
  <div class="brand"><span class="brand-mark"></span>STONECREST</div>
  <nav class="nav">
    <a class="active" href="#">HOME</a>
    <a href="#" style="left:585px">GALLERY</a>
    <a href="#" style="left:677px">QUESTIONS</a>
    <a href="#" style="left:778px">ORDERR</a>
    <a href="#" style="left:866px">SHOPPING CART</a>
  </nav>
  <div class="mini-cart"><i></i><span>Item in your cart<br><b>0 Items</b></span></div>
</header>

<div class="hero-band"></div>
<h1 class="page-title"><i></i>Orders</h1>

<main>
  <div class="panel"></div>
  <div class="head-row" style="top:186px"></div>
  <div class="head-row" style="top:483px"></div>

  <span class="step" style="left:254px;top:195px">1</span><h2 class="step-title" style="left:279px;top:193px">Pick Color</h2>
  <span class="step" style="left:511px;top:195px">2</span><h2 class="step-title" style="left:536px;top:193px">Input Quatities</h2>
  <span class="step" style="left:773px;top:195px">3</span><h2 class="step-title" style="left:800px;top:193px">Get Price</h2>
  <span class="step" style="left:254px;top:492px">4</span><h2 class="step-title" style="left:279px;top:490px">Billing Address</h2>
  <span class="step" style="left:511px;top:492px">5</span><h2 class="step-title" style="left:536px;top:490px">Shipping Method</h2>
  <span class="step" style="left:773px;top:492px">5</span><h2 class="step-title" style="left:800px;top:490px">Review Your Order</h2>
  <span class="step" style="left:511px;top:675px">6</span><h2 class="step-title" style="left:538px;top:673px">Payment Method</h2>

  <div class="field" style="left:261px;top:245px;width:157px"></div>
  <p class="lbl" style="left:264px;top:280px;line-height:16px">See Colors Below Click fun<br>thumbnail for none pictures</p>
  <h3 class="sub-title">Color Pictures</h3>
  <div class="swatch" role="img" aria-label="Amber granite sample" style="left:261px;top:363px;background:#efab2c"></div>
  <div class="swatch" role="img" aria-label="Golden yellow granite sample" style="left:317px;top:363px;background:#f8d213"></div>
  <div class="swatch" role="img" aria-label="Ochre granite sample" style="left:374px;top:363px;background:#c89430"></div>
  <div class="swatch" role="img" aria-label="Brown granite sample" style="left:430px;top:363px;background:#8a6224"></div>
  <div class="swatch" role="img" aria-label="Amber granite sample" style="left:261px;top:417px;background:#eea92a"></div>
  <div class="swatch" role="img" aria-label="Golden yellow granite sample" style="left:317px;top:417px;background:#f6d014"></div>
  <div class="swatch" role="img" aria-label="Ochre granite sample" style="left:374px;top:417px;background:#c18a2e"></div>
  <div class="swatch" role="img" aria-label="Brown granite sample" style="left:430px;top:417px;background:#8c6a28"></div>

  <span class="qty-lbl" style="top:243px">12x12 -</span><span class="qty" style="top:243px"></span>
  <span class="qty-lbl" style="top:266px">12x18 -</span><span class="qty" style="top:266px"></span>
  <span class="qty-lbl" style="top:288px">18x21 -</span><span class="qty" style="top:288px"></span>
  <span class="qty-lbl" style="top:311px">24x24 -</span><span class="qty" style="top:311px"></span>
  <span class="qty-lbl" style="top:333px">ez Ti4 -</span><span class="qty" style="top:333px"></span>
  <span class="qty-lbl" style="top:356px">Bullnese -</span><span class="qty" style="top:356px"></span>
  <span class="qty-lbl" style="top:378px">Leg Left -</span><span class="qty" style="top:378px"></span>
  <span class="qty-lbl" style="top:401px">Leg Right -</span><span class="qty" style="top:401px"></span>
  <span class="qty-lbl" style="top:423px">Inside Coror -</span><span class="qty" style="top:423px"></span>

  <div class="price-card"></div>
  <div class="field" style="left:771px;top:269px;width:158px">Calculate</div>
  <div class="field" style="left:771px;top:307px;width:158px">$XXX</div>
  <div class="btn-cart"><i></i>ADD TO CART</div>
  <svg class="abs" style="left:790px;top:353px" width="18" height="16" viewBox="0 0 18 16"><path d="M1 2h3l2 8h9l2-6H5" fill="none" stroke="#fff" stroke-width="1.8"/><circle cx="7" cy="13" r="1.5" fill="#fff"/><circle cx="14" cy="13" r="1.5" fill="#fff"/></svg>

  <span class="lbl" style="left:264px;top:531px">First Name *</span>
  <span class="lbl" style="left:382px;top:531px">Last Name *</span>
  <div class="field" style="left:261px;top:553px;width:113px"></div>
  <div class="field" style="left:381px;top:553px;width:113px"></div>
  <span class="lbl" style="left:264px;top:582px">Email Adderess *</span>
  <span class="lbl" style="left:382px;top:582px">Telephone*</span>
  <div class="field" style="left:261px;top:603px;width:113px"></div>
  <div class="field" style="left:381px;top:603px;width:113px"></div>
  <span class="lbl" style="left:264px;top:633px">Address *</span>
  <div class="field" style="left:261px;top:653px;width:234px"></div>
  <div class="field" style="left:261px;top:684px;width:234px"></div>
  <span class="lbl" style="left:264px;top:712px">Country *</span>
  <div class="select" style="left:261px;top:735px;width:234px">India<svg width="10" height="7"><path d="M0 0h10L5 7z" fill="#fff"/></svg></div>
  <span class="lbl" style="left:264px;top:764px">City *</span>
  <div class="field" style="left:261px;top:787px;width:234px"></div>
  <span class="lbl" style="left:264px;top:813px">Zip Code *</span>
  <span class="lbl" style="left:384px;top:813px">State *</span>
  <div class="field" style="left:261px;top:836px;width:112px"></div>
  <div class="select" style="left:381px;top:836px;width:112px">Please select<svg width="10" height="7"><path d="M0 0h10L5 7z" fill="#fff"/></svg></div>
  <span class="lbl" style="left:264px;top:863px">Fax</span>
  <div class="field" style="left:261px;top:884px;width:113px"></div>
  <svg class="check" style="left:263px;top:916px" viewBox="0 0 11 11"><rect x=".5" y=".5" width="10" height="10" fill="#eee" stroke="#aaa"/><path d="M2 5.5l2.5 2.5L9 2.5" fill="none" stroke="#333" stroke-width="1.4"/></svg>
  <span class="lbl" style="left:278px;top:915px">Skip to the same address</span>

  <span class="lbl" style="left:533px;top:531px">Wareshouse Picksp</span>
  <span class="radio" style="left:533px;top:553px"></span><span class="lbl" style="left:557px;top:553px">$0.00</span>
  <span class="lbl" style="left:533px;top:570px;line-height:15px">Garage Delivery Within<br>30 miles of 80455</span>
  <span class="radio" style="left:533px;top:603px"></span><span class="lbl" style="left:557px;top:603px">Fixed $55.00</span>
  <span class="lbl" style="left:533px;top:623px">Freight Estmate</span>
  <span class="radio" style="left:533px;top:642px"></span><span class="lbl" style="left:557px;top:642px">Enter Zip Code $0.00</span>

  <span class="radio" style="left:533px;top:697px"></span><span class="lbl" style="left:557px;top:697px">Write a check</span>
  <span class="radio on" style="left:533px;top:721px"></span><span class="lbl" style="left:557px;top:721px">Debit Cart Payment</span>
  <span class="lbl" style="left:535px;top:740px">Credit Cart Type*</span>
  <div class="select" style="left:533px;top:763px;width:168px">-Please Seted<svg width="10" height="7"><path d="M0 0h10L5 7z" fill="#fff"/></svg></div>
  <span class="lbl" style="left:535px;top:786px">Expiration Date*</span>
  <div class="select" style="left:533px;top:807px;width:98px">Month<svg width="10" height="7"><path d="M0 0h10L5 7z" fill="#fff"/></svg></div>
  <div class="select" style="left:639px;top:807px;width:62px">Year<svg width="10" height="7"><path d="M0 0h10L5 7z" fill="#fff"/></svg></div>
  <span class="lbl" style="left:535px;top:831px">Card Verifcation Number*</span>
  <div class="field" style="left:533px;top:854px;width:112px"></div>
  <a class="abs small link" style="left:651px;top:862px;font-size:8px" href="#">What is this?</a>

  <table class="order-table">
    <tr><th style="padding-left:6px">Product</th><th>City</th><th class="num">Subtotal</th></tr>
    <tr><td>Imperial while Long Right</td><td>5</td><td class="num">$129.99</td></tr>
    <tr><td>Imperial while Long Right</td><td>5</td><td class="num">$129.99</td></tr>
    <tr><td>Imperial while Long Right</td><td>5</td><td class="num">$129.99</td></tr>
    <tr class="total"><td></td><td>Subtotal</td><td class="num">$ xxx. xx</td></tr>
    <tr class="total"><td></td><td>Grand total</td><td class="num">$ xxx. xx</td></tr>
  </table>
  <span class="lbl small" style="left:726px;top:694px;font-size:9px">Coments</span>
  <div class="comments"></div>
  <svg class="check" style="left:728px;top:797px" viewBox="0 0 11 11"><rect x=".5" y=".5" width="10" height="10" fill="#eee" stroke="#aaa"/><path d="M2 5.5l2.5 2.5L9 2.5" fill="none" stroke="#333" stroke-width="1.4"/></svg>
  <span class="lbl small" style="left:743px;top:797px">I have read and accept the shipping policy</span>
  <svg class="check" style="left:728px;top:817px" viewBox="0 0 11 11"><rect x=".5" y=".5" width="10" height="10" fill="#eee" stroke="#aaa"/><path d="M2 5.5l2.5 2.5L9 2.5" fill="none" stroke="#333" stroke-width="1.4"/></svg>
  <span class="lbl small" style="left:743px;top:817px">I accept the <a class="link" href="#">Terms and contions</a></span>
  <a class="btn-order" href="#">Place order now</a>
  <div class="panel-foot"></div>
</main>

<div class="below-band"></div>

<footer class="site-footer">
  <a href="#" style="left:252px;top:23px">Home</a>
  <a href="#" style="left:252px;top:45px">Gallery</a>
  <a href="#" style="left:242px;top:67px">› Questions</a>
  <a href="#" style="left:348px;top:23px">› Orderr</a>
  <a href="#" style="left:348px;top:45px">› Shopping Cart</a>
  <a href="#" style="left:348px;top:67px">› Contact Us</a>
  <a href="#" style="left:476px;top:23px">› Return Policy</a>
  <a href="#" style="left:476px;top:45px">› Shipping Policy</a>
  <a href="#" style="left:476px;top:67px">› Privacy</a>
  <a href="#" style="left:596px;top:23px">› Terms of Use</a>
  <a href="#" style="left:596px;top:45px">› Customer Service</a>
</footer>
<div class="foot-brand"><i></i>STONECREST</div>
<p class="copy">© 2011 Stonecrest.com.<br>All Rights Reserved.</p>

</body>
</html>
```